Talents and colours poster for home office

The objective is to illustrate/communicate and remember 5 talents and 4 colours of the personality.

The infographic will be hanged on the wall of an home office. It need to be simple and clear. Illustrations and pictograms can be used. It can be artistic.

Here's the content:

5 talents,scaling in priority from #1 to #5
Ideation / creativity
Winning other over / charisma
Adaptability
Positivity
Empathy

In the files there is a description of what those mean.

You have to include 4 colours, scaling in priority from #1 to #4
Yellow
Green
Red
Blue

I made a sketch just for fun... and to show why I need professionnal skills :)

THX

Industry/Entity Type

Office

Requirements
Should not have
• offensive materials

```html
<!DOCTYPE html>
<html lang="en">
<head>
<meta charset="utf-8">
<title>Talents and Colours</title>
<link rel="stylesheet" href="https://fonts.googleapis.com/css2?family=Noto+Serif:wght@400&display=swap">
<style>
  :root {
    --yellow: #f8ef00;
    --green: #112d0a;
    --red: #cc0000;
    --blue: #000080;
    --ink: #070908;
  }
  html, body {
    margin: 0;
    padding: 0;
    overflow: hidden;
  }
  .poster {
    position: relative;
    width: 929px;
    height: 1200px;
    overflow: hidden;
    font-family: "Noto Serif", Georgia, serif;
    font-weight: 400;
  }
  .band {
    position: absolute;
    left: 0;
    width: 100%;
  }
  .band--yellow { top: 0; height: 300px; background: var(--yellow); }
  .band--green { top: 300px; height: 299px; background: var(--green); }
  .band--red { top: 599px; height: 300px; background: var(--red); }
  .band--blue { top: 899px; height: 301px; background: var(--blue); }

  .talent {
    position: absolute;
    left: 0;
    width: 100%;
    margin: 0;
    text-align: center;
    font-size: 110px;
    line-height: 1;
    font-weight: 400;
    white-space: nowrap;
  }
  .talent--charisma { top: 72px; color: var(--green); }
  .talent--adaptability { top: 355px; color: var(--red); }
  .talent--positivity { top: 721px; color: var(--blue); }
  .talent--empathy { top: 994px; color: var(--yellow); }

  .headline-box {
    position: absolute;
    left: 59px;
    top: 509px;
    width: 817px;
    height: 181px;
    background: var(--ink);
  }
  .headline {
    position: absolute;
    left: 0;
    width: 100%;
    top: 537px;
    margin: 0;
    text-align: center;
    font-size: 120px;
    line-height: 1;
    font-weight: 400;
    letter-spacing: -1px;
    white-space: nowrap;
  }
  .c-yellow { color: var(--yellow); }
  .c-green { color: var(--green); }
  .c-red { color: var(--red); }
  .c-blue { color: var(--blue); }
</style>
</head>
<body>
<main class="poster">
  <div class="band band--yellow"></div>
  <div class="band band--green"></div>
  <div class="band band--red"></div>
  <div class="band band--blue"></div>

  <p class="talent talent--charisma">Charizma</p>
  <p class="talent talent--adaptability">Adaptibility</p>

  <div class="headline-box"></div>
  <h1 class="headline"><span class="c-yellow">C</span><span class="c-green">R</span><span class="c-red">E</span><span class="c-blue">A</span><span class="c-yellow">T</span><span class="c-green">I</span><span class="c-red">V</span><span class="c-blue">I</span><span class="c-yellow">Y</span></h1>

  <p class="talent talent--positivity">Positivity</p>
  <p class="talent talent--empathy">Empathy</p>
</main>
</body>
</html>
```